Meadowgate Bus Card

i own a building in the bronx ny - its called "Meadowgate 5 in 2 HDFC"i want a classy logo / business card - nothing too religuous but it is like a family there - its a large apartment building - colors i like dark red, black, medium shade of gray also reg business card stuff tel # 914-552-3917 address 3182 Larkwell Ave Bronx NY 10472 Email fijosh@aol.comslogan - " Together Under One Roof "i can send u a picture of the building for the backside

```html
<!DOCTYPE html>
<html lang="en">
<head>
<meta charset="utf-8">
<title>Meadowgate 5 in 2 HDFC – Business Card</title>
<link rel="stylesheet" href="https://fonts.googleapis.com/css2?family=Montserrat:wght@600;700&family=Open+Sans:wght@400;600&display=swap">
<style>
  :root {
    --backdrop: #3b3532;
    --card: #0f0f0f;
    --gold: #f2b318;
    --silver: #c4c4c4;
    --text-light: #d6d6d6;
    --white: #f2f2f2;
    --rule: #4a4a4a;
  }
  * { box-sizing: border-box; margin: 0; padding: 0; }
  html, body {
    width: 1200px; height: 844px; overflow: hidden;
    background: var(--backdrop);
  }
  .canvas { position: relative; width: 1200px; height: 844px; }
  .card {
    position: absolute; top: 272px;
    width: 520px; height: 300px;
    background: var(--card);
    border-radius: 3px;
    box-shadow: 0 10px 30px rgba(0,0,0,.45);
  }
  .card--front { left: 60px; }
  .card--back { left: 620px; }

  /* front */
  .brand {
    position: absolute; left: 18px; top: 100px; width: 236px;
    display: flex; flex-direction: column; align-items: center;
  }
  .brand__mark {
    width: 24px; height: 24px; border-radius: 50%;
    background: var(--silver); margin-bottom: 12px;
  }
  .brand__name {
    font-family: "Montserrat", sans-serif; font-weight: 600;
    font-size: 16px; line-height: 1.2; white-space: nowrap;
    color: var(--white);
  }
  .divider {
    position: absolute; left: 262px; top: 28px;
    width: 1px; height: 170px; background: var(--rule);
  }
  .contact {
    position: absolute; left: 286px; top: 36px;
    font-family: "Open Sans", sans-serif; color: var(--text-light);
    font-size: 13px; line-height: 1.45;
  }
  .contact__name {
    font-family: "Montserrat", sans-serif; font-weight: 700;
    font-size: 15px; color: var(--gold); text-transform: uppercase;
  }
  .contact__title { margin-bottom: 12px; }
  .contact__row { display: flex; align-items: center; gap: 8px; }
  .contact__row svg { width: 11px; height: 11px; fill: var(--gold); flex: none; }
  .contact__address { margin-top: 10px; padding-left: 19px; }
  .slogan {
    position: absolute; left: 0; right: 0; bottom: 40px;
    text-align: center;
    font-family: "Montserrat", sans-serif; font-weight: 700;
    font-size: 15px; letter-spacing: 1px; color: var(--white);
    text-transform: uppercase;
  }

  /* back */
  .back-brand {
    position: absolute; left: 0; right: 0; top: 110px;
    display: flex; flex-direction: column; align-items: center;
  }
  .back-brand__mark {
    width: 30px; height: 30px; border-radius: 50%;
    background: var(--silver); margin-bottom: 14px;
  }
  .back-brand__name {
    font-family: "Montserrat", sans-serif; font-weight: 600;
    font-size: 24px; color: var(--silver); white-space: nowrap;
  }
</style>
</head>
<body>
<main class="canvas">
  <section class="card card--front">
    <div class="brand">
      <span class="brand__mark"></span>
      <p class="brand__name">Meadowgate 5 in 2 HDFC</p>
    </div>
    <span class="divider"></span>
    <div class="contact">
      <p class="contact__name">Marcus Delaney</p>
      <p class="contact__title">Managing Director</p>
      <p class="contact__row">
        <svg viewBox="0 0 24 24" aria-hidden="true"><path d="M6.6 10.8a15.1 15.1 0 0 0 6.6 6.6l2.2-2.2a1 1 0 0 1 1-.25 11.4 11.4 0 0 0 3.6.57 1 1 0 0 1 1 1V20a1 1 0 0 1-1 1A17 17 0 0 1 3 4a1 1 0 0 1 1-1h3.5a1 1 0 0 1 1 1c0 1.25.2 2.45.57 3.57a1 1 0 0 1-.25 1z"/></svg>
        914-552-3917
      </p>
      <p class="contact__row">
        <svg viewBox="0 0 24 24" aria-hidden="true"><path d="M2 5h20v14H2zm2 2v.5l8 5 8-5V7l-8 5z"/></svg>
        kemarv@plonkmail.test
      </p>
      <p class="contact__address">3182 Larkwell Ave<br>Bronx NY 10472</p>
    </div>
    <p class="slogan">Together Under One Roof</p>
  </section>

  <section class="card card--back">
    <div class="back-brand">
      <span class="back-brand__mark"></span>
      <p class="back-brand__name">Meadowgate 5 in 2 HDFC</p>
    </div>
  </section>
</main>
</body>
</html>
```